Veradine Contracting Folder

Creating a design for the cover of our folders that we pass to our customers

Want to keep the same look as our colors and fonts as attached

```html
<!DOCTYPE html>
<html lang="en">
<head>
<meta charset="utf-8">
<title>Veradine Contracting Folder</title>
<link rel="stylesheet" href="https://fonts.googleapis.com/css2?family=Questrial&display=swap">
<style>
  :root {
    --navy: #38418a;
    --navy-light: #6670a8;
    --gold: #e0c150;
    --lavender: #a9abcf;
    --paper: #ececea;
    --stage: #dcdcdc;
    --divider: #ffffff;
  }
  html, body {
    margin: 0;
    padding: 0;
    width: 1200px;
    height: 1200px;
    overflow: hidden;
    background: var(--divider);
  }
  .sheet {
    position: relative;
    width: 1200px;
    height: 1200px;
  }
  .view {
    position: absolute;
    background: var(--stage);
    display: flex;
    align-items: center;
    justify-content: center;
  }
  .view--front { left: 0; top: 0; width: 1200px; height: 776px; }
  .view--back { left: 0; top: 788px; width: 594px; height: 412px; }
  .view--inside { left: 606px; top: 788px; width: 594px; height: 412px; }
  svg { display: block; box-shadow: 0 6px 18px rgba(0,0,0,0.12); }
  .company-name {
    font-family: "Questrial", "Helvetica", sans-serif;
    font-weight: 400;
    fill: var(--navy);
  }
  .contact-line {
    font-family: "Questrial", "Helvetica", sans-serif;
    fill: var(--gold);
    letter-spacing: 1px;
  }
</style>
</head>
<body>
<main class="sheet">

  <section class="view view--front" aria-label="Folder front cover">
    <svg class="cover-front" width="500" height="660" viewBox="0 0 500 660">
      <defs>
        <linearGradient id="navyFade" x1="0" y1="1" x2="1" y2="0">
          <stop offset="0" stop-color="var(--navy)"/>
          <stop offset="1" stop-color="var(--navy-light)"/>
        </linearGradient>
      </defs>
      <rect class="cover-paper" width="500" height="660" fill="var(--paper)"/>
      <polygon class="cover-gold-wedge" points="0,0 500,0 0,190" fill="var(--gold)"/>
      <polygon class="cover-navy-field" points="0,570 500,250 500,660 0,660" fill="url(#navyFade)"/>
      <g class="company-title">
        <circle class="company-dot" cx="92" cy="238" r="8" fill="var(--navy)"/>
        <text class="company-name" x="112" y="250" font-size="30">Veradine Contracting</text>
      </g>
    </svg>
  </section>

  <section class="view view--back" aria-label="Folder back cover">
    <svg class="cover-back" width="270" height="350" viewBox="0 0 270 350">
      <defs>
        <linearGradient id="navyFadeBack" x1="0" y1="0" x2="1" y2="1">
          <stop offset="0" stop-color="var(--navy-light)"/>
          <stop offset="1" stop-color="var(--navy)"/>
        </linearGradient>
      </defs>
      <rect width="270" height="350" fill="var(--paper)"/>
      <polygon class="back-gold-field" points="0,0 270,0 270,175 0,70" fill="var(--gold)"/>
      <polygon class="back-navy-wedge" points="0,245 0,350 245,350" fill="url(#navyFadeBack)"/>
      <rect class="back-lavender-band" x="118" y="0" width="40" height="350" fill="var(--lavender)"/>
      <text class="company-name" x="138" y="199" font-size="11" text-anchor="middle" transform="rotate(-90 138 195)">Veradine</text>
      <g class="back-contact">
        <text class="contact-line" x="8" y="318" font-size="6">VERADINE CONTRACTING</text>
        <text class="contact-line" x="8" y="328" font-size="6">PAINTING SERVICES DAILY</text>
        <text class="contact-line" x="8" y="338" font-size="6">WWW.VERADINE.EXAMPLE</text>
      </g>
    </svg>
  </section>

  <section class="view view--inside" aria-label="Folder inside spread">
    <svg class="inside-spread" width="460" height="300" viewBox="0 0 460 300">
      <defs>
        <linearGradient id="navyFadeInside" x1="0" y1="0" x2="1" y2="0">
          <stop offset="0" stop-color="var(--navy-light)"/>
          <stop offset="1" stop-color="var(--navy)"/>
        </linearGradient>
      </defs>
      <rect width="460" height="300" fill="var(--paper)"/>
      <polygon class="inside-navy-field" points="0,0 460,0 460,40 0,175" fill="url(#navyFadeInside)"/>
      <polygon class="inside-gold-wedge" points="0,255 230,238 230,300 0,300" fill="var(--gold)"/>
      <line class="inside-fold" x1="230" y1="0" x2="230" y2="300" stroke="#d4d4d4" stroke-width="1"/>
      <g class="inside-pocket">
        <path d="M250 110 H460 V300 H250 Z" fill="#f3f3f1" stroke="#dadada"/>
        <polygon points="370,110 460,110 460,175" fill="var(--navy)"/>
        <path class="pocket-tab" d="M330 300 V250 Q330 215 365 215 H460 V300 Z" fill="var(--gold)"/>
        <text class="company-name" x="300" y="170" font-size="15" text-anchor="middle">Veradine</text>
      </g>
    </svg>
  </section>

</main>
</body>
</html>
```